Women's Online Clothing Boutique Needs Business Cards

I already have a logo that I would like to use. Some of the things that interest me is black business cards, foil embossed logo, glossy embossed logo, leopard print, no yellow font, rounded edges. I even like just a large logo on the front side with all of my information on the back side.

Contact Information for Business Card

https://copperfinch.shopvendly.example/
https://www.facebook.com/thecopperfinchboutique/
https://www.instagram.com/thecopperfinchboutique/
copperfinchboutique@mailora.example

Requirements
Must have
• My Logo
Nice to have
• Leopard Print
Should not have
• No Yellow Font

```html
<!DOCTYPE html>
<html lang="en">
<head>
<meta charset="utf-8">
<title>The Copper Finch Boutique – Business Card</title>
<link href="https://fonts.googleapis.com/css2?family=Poppins:wght@400;500&display=swap" rel="stylesheet">
<style>
  :root {
    --page: #e6e6e6;
    --card: #0b0b0b;
    --gold: #c9a25a;
    --gold-soft: #a8843f;
    --white: #f2f2f2;
    --grey: #8a8a8a;
  }
  * { box-sizing: border-box; margin: 0; padding: 0; }
  html, body {
    width: 1200px; height: 965px; overflow: hidden;
    background: var(--page);
    font-family: "Poppins", sans-serif;
  }
  .sheet {
    position: relative; width: 1200px; height: 965px;
    display: flex; flex-direction: column; align-items: center;
    justify-content: center; gap: 32px;
  }
  .card {
    position: relative; width: 760px; height: 434px;
    background: var(--card); border-radius: 16px; overflow: hidden;
  }
  .rule { position: absolute; height: 1.5px; background: var(--gold); }
  .brand {
    position: absolute; left: 0; right: 0; text-align: center;
    color: var(--gold); font-weight: 500; line-height: 1.1;
  }
  .brand-mark {
    display: inline-block; border-radius: 50%;
    background: var(--gold); vertical-align: middle;
  }

  /* front */
  .card-front .brand { top: 150px; font-size: 46px; letter-spacing: 0.5px; }
  .card-front .brand .brand-mark { width: 22px; height: 22px; margin-right: 14px; }
  .card-front .brand small { display: block; font-size: 30px; margin-top: 6px; }
  .card-front .rule-top { left: 370px; right: 0; top: 128px; }
  .card-front .rule-bottom { left: 0; right: 380px; top: 292px; }

  /* back */
  .card-back .brand { top: 110px; font-size: 32px; }
  .card-back .brand .brand-mark { width: 16px; height: 16px; margin-right: 10px; }
  .card-back .brand small { display: block; font-size: 22px; margin-top: 4px; }
  .card-back .rule-left { left: 0; width: 190px; top: 150px; }
  .card-back .rule-right { right: 0; width: 190px; top: 150px; }

  .holder { position: absolute; left: 48px; bottom: 58px; }
  .holder-name { color: var(--gold); font-size: 28px; font-weight: 500; }
  .holder-role { color: var(--white); font-size: 17px; margin-top: 2px; text-align: right; }

  .divider { position: absolute; left: 372px; bottom: 46px; width: 1.5px; height: 120px; background: var(--grey); }

  .contacts { position: absolute; left: 398px; bottom: 48px; list-style: none; }
  .contacts li {
    display: flex; align-items: center; gap: 10px;
    color: var(--white); font-size: 15.5px; line-height: 29px;
  }
  .contacts .dot { width: 15px; height: 15px; border-radius: 50%; background: var(--gold); flex: none; }
  .contacts svg { width: 16px; height: 16px; flex: none; }
  .contacts .hl { color: var(--gold); }
</style>
</head>
<body>
<main class="sheet">
  <section class="card card-front" aria-label="Card front">
    <div class="rule rule-top"></div>
    <div class="rule rule-bottom"></div>
    <div class="brand"><span class="brand-mark"></span>The Copper Finch<small>Boutique</small></div>
  </section>

  <section class="card card-back" aria-label="Card back">
    <div class="rule rule-left"></div>
    <div class="rule rule-right"></div>
    <div class="brand"><span class="brand-mark"></span>The Copper Finch<small>Boutique</small></div>

    <div class="holder">
      <p class="holder-name">Dana Wrenfield</p>
      <p class="holder-role">Owner / CEO</p>
    </div>
    <div class="divider"></div>

    <ul class="contacts">
      <li><span class="dot"></span>thecopperfinchboutique</li>
      <li><span class="dot"></span>thecopperfinchboutique</li>
      <li>
        <svg viewBox="0 0 16 16" fill="none" stroke="#c9a25a" stroke-width="1.3"><rect x="1.5" y="3.5" width="13" height="9"/><path d="M1.5 3.5 8 9l6.5-5.5"/></svg>
        copperfinchboutique@mailora.example
      </li>
      <li>
        <svg viewBox="0 0 16 16" fill="none" stroke="#c9a25a" stroke-width="1.3"><circle cx="8" cy="8" r="6.5"/><ellipse cx="8" cy="8" rx="2.8" ry="6.5"/><path d="M1.5 8h13M2.5 5h11M2.5 11h11"/></svg>
        <span><span class="hl">copperfinch</span>.shopvendly.example</span>
      </li>
    </ul>
  </section>
</main>
</body>
</html>
```